Venture Capital Investment Firm

We are looking to overhaul our existing website (substantially), with only using the same logos (which we can provide).
We are an investment firm that focuses on making loans to late stage technology companies. Our site should ultimately look like other venture capital firms, and look modern and fresh. We have an existing website www.northvaleloan.com which this will be replacing, although we will be using a lot of the existing written content, and potentially the numbers of pages we will need, we are not wed to anything else. Please feel free to shoot any questions at any time and thank you in advance for your help!
Websites we like as examples:
https://www.tkbrandel.com/
https://www.emberwoodfunds.com/
Target Market(s)
Potential investors who will invest in our firm, as well as potentially companies that are looking to borrow money from us.

```html
<!DOCTYPE html>
<html lang="en">
<head>
<meta charset="utf-8">
<title>Northvale Loan — Exceptional Investments</title>
<link href="https://fonts.googleapis.com/css2?family=Merriweather:wght@400;700;900&family=Open+Sans:wght@400;600;700&display=swap" rel="stylesheet">
<style>
:root{
  --gold:#d0ab4a;
  --gold-dark:#b8953a;
  --ink:#1b1b1b;
  --dark:#1e1f21;
  --text:#2a2a2a;
  --muted:#777;
  --white:#fff;
  --light:#f4f4f4;
}
*{box-sizing:border-box;margin:0;padding:0}
html,body{width:1200px;height:4212px;overflow:hidden}
body{position:relative;background:var(--white);font-family:"Open Sans",Arial,sans-serif;color:var(--text)}
.abs{position:absolute}
.center{text-align:center}

/* header */
.site-header{position:absolute;left:0;top:0;width:1200px;height:85px;background:var(--ink)}
.brand{position:absolute;left:188px;top:24px;display:flex;align-items:center;gap:10px}
.brand-dot{width:30px;height:30px;border:3px solid var(--gold);border-radius:50%}
.brand-name{font-family:"Merriweather",Georgia,serif;color:var(--gold);font-size:19px;font-weight:400;letter-spacing:.5px;line-height:1}
.brand-sub{display:block;font-family:"Merriweather",Georgia,serif;font-size:7px;letter-spacing:.6px;margin-top:3px}
.main-nav{position:absolute;left:556px;top:36px;display:flex;gap:28px}
.main-nav a{color:#eee;text-decoration:none;font-size:11px;font-weight:600;letter-spacing:.3px}
.main-nav a.active{color:var(--gold)}

/* hero */
.hero-photo{left:0;top:85px;width:1200px;height:561px;background:linear-gradient(180deg,#5d6670 0%,#7f8890 45%,#4a535c 100%)}
.hero-panel{left:200px;top:225px;width:372px;height:257px;background:rgba(40,40,44,.55)}
.bracket-tl{left:198px;top:246px;width:84px;height:76px;border-left:5px solid var(--gold);border-top:5px solid var(--gold)}
.bracket-br{left:444px;top:364px;width:84px;height:76px;border-right:5px solid var(--gold);border-bottom:5px solid var(--gold)}
.hero-title{left:230px;top:270px;color:#fff;font-family:"Merriweather",serif;font-weight:900;font-size:38px;line-height:51px}
.hero-sub{left:230px;top:374px;color:#fff;font-family:"Merriweather",serif;font-size:21px;letter-spacing:.5px}
.hero-arrows{left:230px;top:412px;display:flex;gap:16px}
.hero-arrows span{width:23px;height:23px;border:2px solid #fff;border-radius:50%;display:flex;align-items:center;justify-content:center}

/* intro box */
.intro-box{left:188px;top:481px;width:824px;height:289px;background:var(--gold)}
.intro-icon{left:36px;top:70px}
.intro-title{left:177px;top:32px;width:600px;color:#fff;font-family:"Merriweather",serif;font-weight:900;font-size:23px;line-height:34px}
.intro-text{left:177px;top:110px;width:620px;color:#fff;font-size:9.5px;line-height:15.5px}
.intro-text p+p{margin-top:12px}

/* section titles */
.sec-title{width:1200px;left:0;text-align:center;font-family:"Merriweather",serif;font-weight:700;font-size:25px;color:var(--ink)}
.sec-title.light{color:#fff}
.sec-mark{left:591px;width:18px;height:18px;border:3px solid var(--gold);border-radius:50%}
.sec-lead{left:375px;width:450px;text-align:center;font-size:9.5px;line-height:16px;color:#555}
.sec-lead.light{color:#ddd}

/* services */
.service{top:1009px;width:253px;height:283px;text-align:center}
.service.raised{background:#fff;box-shadow:0 2px 10px rgba(0,0,0,.25)}
.service svg{margin-top:38px}
.service h3{font-family:"Merriweather",serif;font-size:15px;font-weight:700;margin-top:20px;color:var(--ink)}
.service .rule{width:36px;height:2px;background:var(--gold);margin:10px auto 14px}
.service p{font-size:9.5px;line-height:15.5px;color:#666;padding:0 28px}
.btn-gold{left:533px;top:1331px;width:136px;height:39px;background:var(--gold);color:#fff;font-size:10.5px;font-weight:600;display:flex;align-items:center;justify-content:center;box-shadow:2px 3px 6px rgba(0,0,0,.3)}

/* testimonial */
.testimonial-bg{left:0;top:1467px;width:1200px;height:441px;background:linear-gradient(90deg,#17191d 0%,#1f2226 55%,#3a3d41 80%,#1a1c1f 100%)}
.portrait{left:305px;top:1662px;width:130px;height:130px;border-radius:50%;border:4px solid var(--gold);background:radial-gradient(circle at 50% 45%,#cfd5da,#8a97a3)}
.quote{left:481px;top:1670px;width:410px;color:#ccc;font-size:9.5px;line-height:16px}
.quote-name{left:481px;top:1738px;color:var(--gold);font-family:"Merriweather",serif;font-size:13px}
.quote-role{left:481px;top:1761px;color:#ddd;font-size:12px}
.dots{left:568px;top:1832px;display:flex;gap:6px}
.dots span{width:8px;height:8px;border-radius:50%;background:#ddd}
.dots span.on{background:var(--gold)}

/* team */
.member{top:2142px;width:265px;height:214px;background:linear-gradient(180deg,#3a3a3a,#111)}
.member-tag{top:2302px;width:163px;height:69px;background:var(--gold);text-align:center;color:#fff}
.member-tag h4{font-family:"Merriweather",serif;font-size:15px;font-weight:700;margin-top:10px}
.member-tag .rule{width:30px;height:2px;background:#fff;margin:7px auto 6px}
.member-tag small{font-size:7px;letter-spacing:.5px;display:block}

/* facts */
.facts-bg{left:0;top:2518px;width:1200px;height:414px;background:linear-gradient(135deg,#1b2530 0%,#2a3846 50%,#1a2330 100%)}
.fact{top:2740px;width:200px;text-align:center;color:#fff}
.fact .num{font-family:"Merriweather",serif;font-weight:700;font-size:42px;margin-top:14px;line-height:50px}
.fact .label{font-size:13px;color:#ddd;margin-top:2px}
.fact-divider{top:2788px;width:2px;height:82px;background:#fff}

/* news */
.news-card{top:3157px;width:253px;height:370px;background:var(--light)}
.news-img{height:214px}
.news-meta{display:flex;justify-content:space-between;font-size:6.5px;color:#777;padding:20px 18px 0}
.news-meta b{color:var(--gold);font-weight:400}
.news-card h3{font-family:"Merriweather",serif;font-size:14px;font-weight:700;line-height:20px;padding:10px 18px 0;color:var(--ink)}
.news-card p{font-size:9.5px;line-height:15.5px;color:#888;padding:6px 18px 0}

/* partners */
.partners{left:0;top:3626px;width:1200px;height:164px;background:var(--gold)}
.partner{top:3692px;color:#fff;font-family:"Merriweather",serif;font-size:21px;display:flex;align-items:center;gap:10px;white-space:nowrap}
.partner i{width:24px;height:24px;border:3px solid #fff;border-radius:50%}

/* footer */
.site-footer{left:0;top:3790px;width:1200px;height:422px;background:var(--dark)}
.foot-title{color:var(--gold);font-family:"Merriweather",serif;font-size:22px;font-weight:700;text-align:center}
.foot-text{color:#bbb;font-size:9.5px;line-height:15.5px;text-align:center}
.social{left:242px;top:4039px;display:flex;gap:13px}
.social span{width:24px;height:24px;border:2px solid var(--gold);border-radius:50%}
.email-field{left:544px;top:3976px;width:223px;height:35px;border:1px solid #bbb;color:#aaa;font-size:8px;display:flex;align-items:center;justify-content:center}
.btn-send{left:587px;top:4028px;width:137px;height:35px;background:var(--gold);border-radius:18px;color:#fff;font-size:9.5px;font-weight:700;display:flex;align-items:center;justify-content:center}
.contact-line{color:#bbb;font-size:9.5px;display:flex;align-items:flex-start;gap:10px}
.to-top{left:1084px;top:3970px;width:44px;height:36px;background:var(--gold);display:flex;align-items:center;justify-content:center}
.foot-rule{left:188px;top:4141px;width:824px;height:1px;background:#555}
.copyright{left:188px;top:4171px;color:#aaa;font-size:9.5px}
.foot-nav{left:722px;top:4171px;display:flex;gap:15px}
.foot-nav a{color:#aaa;font-size:9.5px;text-decoration:none}
</style>
</head>
<body>

<header class="site-header">
  <div class="brand">
    <span class="brand-dot"></span>
    <span class="brand-name">NORTHVALE LOAN<span class="brand-sub">LOAN PARTNERS, LLC</span></span>
  </div>
  <nav class="main-nav">
    <a class="active" href="#">HOME</a><a href="#">STRATEGY</a><a href="#">ABOUT US</a><a href="#">TEAM</a><a href="#">NEWS</a><a href="#">INVESTORS</a><a href="#">CONTACT</a>
  </nav>
</header>

<section>
  <div class="abs hero-photo" role="img" aria-label="Businessman on a high balcony looking over a city skyline"></div>
  <div class="abs hero-panel"></div>
  <div class="abs bracket-tl"></div>
  <div class="abs bracket-br"></div>
  <h1 class="abs hero-title">Exceptional<br>Investments,</h1>
  <div class="abs hero-sub">EXTRAORDINARY WORLD</div>
  <div class="abs hero-arrows">
    <span><svg width="10" height="10" viewBox="0 0 10 10"><path d="M6 2 3 5l3 3" stroke="#fff" stroke-width="1.6" fill="none"/></svg></span>
    <span><svg width="10" height="10" viewBox="0 0 10 10"><path d="M4 2l3 3-3 3" stroke="#fff" stroke-width="1.6" fill="none"/></svg></span>
  </div>
</section>

<section class="abs intro-box">
  <svg class="abs intro-icon" width="100" height="150" viewBox="0 0 100 150" fill="none" stroke="#fff" stroke-width="5">
    <path d="M50 8C26 8 10 26 10 48c0 16 10 26 18 36 4 6 6 12 6 18h32c0-6 2-12 6-18 8-10 18-20 18-36C90 26 74 8 50 8z"/>
    <path d="M34 114h32M36 126h28M42 138h16" stroke-linecap="round"/>
  </svg>
  <h2 class="abs intro-title">FINANCE PROVEN INNOVATION WITH A DIFFERENT APPROACH</h2>
  <div class="abs intro-text">
    <p>Northvale Loan is a private investment firm unique in its dual focus on life science and technology credit opportunities. Our ambidextrous approach to investing reflects a broad recognition and appreciation for the critical role intellectual property plays in the successful commercialization of products. We apply our extensive industry expertise to assess the revenue visibility created by these assets and offer a range of creative financing solutions.</p>
    <p>A pioneer in providing life science structured credit beginning in 2004, the Northvale team was the first to introduce flexible structured credit to the technology sector in 2014. Our team was also early to recognize the potential of "non-core" assets beyond drug royalties, acquiring over $300M of branded generics offering predictable cash flows from large pharmaceutical firms and partnering with entrepreneurial teams to successfully manage these brands.</p>
  </div>
</section>

<section>
  <h2 class="abs sec-title" style="top:838px">Our Services</h2>
  <div class="abs sec-mark" style="top:882px"></div>
  <p class="abs sec-lead" style="top:914px">Our focus spans the life science and technology industries, two sectors where intellectual property (IP) is an integral driver of asset and enterprise value. Our broad experience in investing, technology evaluation, and product forecasting affords us a unique understanding of the value of assets in these dynamic sectors, allowing us to see value where others cannot.</p>

  <div class="abs service raised" style="left:188px">
    <svg width="78" height="70" viewBox="0 0 78 70"><rect x="2" y="2" width="74" height="50" rx="5" fill="#d0ab4a"/><rect x="32" y="52" width="14" height="10" fill="#d0ab4a"/><rect x="20" y="62" width="38" height="5" fill="#d0ab4a"/><circle cx="39" cy="30" r="11" fill="none" stroke="#fff" stroke-width="4"/><circle cx="56" cy="18" r="6" fill="none" stroke="#fff" stroke-width="3"/></svg>
    <h3>Software &amp; Services</h3><div class="rule"></div>
    <p>Lorem Ipsum is simply dummy text of the printing and typesetting industry. Lorem Ipsum has been the industry's standard dummy text ever since the 1500s.</p>
  </div>
  <div class="abs service" style="left:473px">
    <svg width="78" height="70" viewBox="0 0 78 70"><rect x="14" y="6" width="50" height="56" rx="4" fill="none" stroke="#d0ab4a" stroke-width="5"/><rect x="28" y="22" width="22" height="24" fill="none" stroke="#d0ab4a" stroke-width="4"/><path d="M22 0v6M30 0v6M38 0v6M46 0v6M54 0v6M22 62v6M30 62v6M38 62v6M46 62v6M54 62v6M8 14h6M8 24h6M8 34h6M8 44h6M8 54h6M64 14h6M64 24h6M64 34h6M64 44h6M64 54h6" stroke="#d0ab4a" stroke-width="3"/></svg>
    <h3>Hardware</h3><div class="rule"></div>
    <p>Lorem Ipsum is simply dummy text of the printing and typesetting industry. Lorem Ipsum has been the industry's standard dummy text ever since the 1500s.</p>
  </div>
  <div class="abs service" style="left:759px">
    <svg width="78" height="70" viewBox="0 0 78 70"><rect x="2" y="2" width="74" height="50" rx="5" fill="#d0ab4a"/><rect x="32" y="52" width="14" height="10" fill="#d0ab4a"/><rect x="20" y="62" width="38" height="5" fill="#d0ab4a"/><circle cx="39" cy="30" r="11" fill="none" stroke="#fff" stroke-width="4"/><circle cx="56" cy="18" r="6" fill="none" stroke="#fff" stroke-width="3"/></svg>
    <h3>Systems</h3><div class="rule"></div>
    <p>Lorem Ipsum is simply dummy text of the printing and typesetting industry. Lorem Ipsum has been the industry's standard dummy text ever since the 1500s.</p>
  </div>
  <div class="abs btn-gold">VIEW ALL LAWS</div>
</section>

<section>
  <div class="abs testimonial-bg" role="img" aria-label="Dark photo of a bearded man reading his phone"></div>
  <h2 class="abs sec-title light" style="top:1532px">What People Say</h2>
  <div class="abs sec-mark" style="top:1576px"></div>
  <p class="abs sec-lead light" style="top:1603px">Lorem Ipsum is simply dummy text of the printing and typesetting industry. Lorem Ipsum has been the industry's standard dummy text ever since the 1500s.</p>
  <div class="abs portrait" role="img" aria-label="Portrait of the client giving the testimonial"></div>
  <p class="abs quote">Lorem Ipsum is simply dummy text of the printing and typesetting industry. Lorem Ipsum has been the industry's standard dummy text ever since the 1500s. Lorem Ipsum is simply dummy text of the printing.</p>
  <div class="abs quote-name">Dalen Ferro</div>
  <div class="abs quote-role">Halvik</div>
  <div class="abs dots"><span></span><span></span><span class="on"></span><span></span><span></span></div>
</section>

<section>
  <h2 class="abs sec-title" style="top:2005px">Team of Professionals</h2>
  <div class="abs sec-mark" style="top:2050px"></div>
  <p class="abs sec-lead" style="top:2076px">Lorem Ipsum is simply dummy text of the printing and typesetting industry. Lorem Ipsum has been the industry's standard dummy text ever since the 1500s.</p>

  <div class="abs member" style="left:188px" role="img" aria-label="Black and white portrait of a managing partner"></div>
  <div class="abs member" style="left:467px" role="img" aria-label="Black and white portrait of a managing partner"></div>
  <div class="abs member" style="left:747px" role="img" aria-label="Black and white portrait of a partner"></div>
  <div class="abs member-tag" style="left:239px"><h4>Miles Corvan</h4><div class="rule"></div><small>MANAGING PARTNER</small></div>
  <div class="abs member-tag" style="left:518px"><h4>Tariq Olwen</h4><div class="rule"></div><small>MANAGING PARTNER</small></div>
  <div class="abs member-tag" style="left:798px"><h4>Owen Hartley</h4><div class="rule"></div><small>PARTNER</small></div>
</section>

<section>
  <div class="abs facts-bg" role="img" aria-label="Dark blue photo of a desk with a laptop"></div>
  <h2 class="abs sec-title light" style="top:2577px">Facts and Numbers</h2>
  <div class="abs sec-mark" style="top:2620px"></div>
  <p class="abs sec-lead light" style="top:2649px">Lorem Ipsum is simply dummy text of the printing and typesetting industry. Lorem Ipsum has been the industry's standard dummy text ever since the 1500s.</p>

  <div class="abs fact" style="left:211px">
    <svg width="46" height="38" viewBox="0 0 46 38" fill="none" stroke="#d0ab4a" stroke-width="2"><path d="M2 14l10-10 11 8 11-8 10 10M12 4l-4 20 10 10 14-12M34 4l4 20-10 10"/></svg>
    <div class="num">1450</div><div class="label">Trusted Clients</div>
  </div>
  <div class="abs fact" style="left:395px">
    <svg width="46" height="38" viewBox="0 0 46 38" fill="none" stroke="#d0ab4a" stroke-width="2"><path d="M13 2h20v10a10 10 0 0 1-20 0zM13 6H6c0 6 3 9 8 9M33 6h7c0 6-3 9-8 9M23 22v8M15 36h16M18 30h10v6H18z"/></svg>
    <div class="num">18</div><div class="label">Awards</div>
  </div>
  <div class="abs fact" style="left:595px">
    <svg width="46" height="38" viewBox="0 0 46 38" fill="none" stroke="#d0ab4a" stroke-width="2"><path d="M4 36l10-10 8 6 18-22M32 8h9v9M10 36V30M18 36v-4M26 36V26M34 36V20"/></svg>
    <div class="num">21</div><div class="label">Years of Experience</div>
  </div>
  <div class="abs fact" style="left:801px">
    <svg width="46" height="38" viewBox="0 0 46 38" fill="none" stroke="#d0ab4a" stroke-width="2"><circle cx="23" cy="9" r="6"/><path d="M13 36V24a10 8 0 0 1 20 0v12"/><circle cx="8" cy="15" r="4"/><circle cx="38" cy="15" r="4"/><path d="M2 34v-8a6 5 0 0 1 9-4M44 34v-8a6 5 0 0 0-9-4"/></svg>
    <div class="num">16k</div><div class="label">Experts</div>
  </div>
  <div class="abs fact-divider" style="left:401px"></div>
  <div class="abs fact-divider" style="left:588px"></div>
  <div class="abs fact-divider" style="left:800px"></div>
</section>

<section>
  <h2 class="abs sec-title" style="top:3012px">Latest News</h2>
  <div class="abs sec-mark" style="top:3056px"></div>
  <p class="abs sec-lead" style="top:3085px">Lorem Ipsum is simply dummy text of the printing and typesetting industry. Lorem Ipsum has been the industry's standard dummy text ever since the 1500s.</p>

  <article class="abs news-card" style="left:188px">
    <div class="news-img" style="background:linear-gradient(135deg,#7a6a58,#3a3430)" role="img" aria-label="Man at a desk checking his phone beside glasses"></div>
    <div class="news-meta"><span>JUNE 14, 2018</span><span>BY <b>ADMIN</b></span></div>
    <h3>What's the Right Asset Allocation For Investors?</h3>
    <p>Lorem Ipsum is simply dummy text of the printing and typesetting industry. Lorem Ipsum has been the industry's standard dummy text ever since the 1500s.</p>
  </article>
  <article class="abs news-card" style="left:473px">
    <div class="news-img" style="background:linear-gradient(135deg,#9fb3c4,#5a6f82)" role="img" aria-label="Glasses and papers on a desk next to a laptop"></div>
    <div class="news-meta"><span>JUNE 14, 2018</span><span>BY <b>ADMIN</b></span></div>
    <h3>How Return Assumptions Affect Investor Behavior?</h3>
    <p>Lorem Ipsum is simply dummy text of the printing and typesetting industry. Lorem Ipsum has been the industry's standard dummy text ever since the 1500s.</p>
  </article>
  <article class="abs news-card" style="left:757px">
    <div class="news-img" style="background:linear-gradient(135deg,#4e5862,#8a7a68)" role="img" aria-label="Businessman on a phone call near a window"></div>
    <div class="news-meta"><span>JUNE 14, 2018</span><span>BY <b>ADMIN</b></span></div>
    <h3>Why Money Manager Due Diligence is so Difficult?</h3>
    <p>Lorem Ipsum is simply dummy text of the printing and typesetting industry. Lorem Ipsum has been the industry's standard dummy text ever since the 1500s.</p>
  </article>
</section>

<section class="abs partners"></section>
<div class="abs partner" style="left:188px"><i></i>Vantrel</div>
<div class="abs partner" style="left:362px">Quillby Bank</div>
<div class="abs partner" style="left:540px">Orvessa Post</div>
<div class="abs partner" style="left:714px">Dunmere Bank</div>
<div class="abs partner" style="left:900px"><i></i>Zelko</div>

<footer class="abs site-footer"></footer>
<div class="abs" style="left:242px;top:3873px;display:flex;align-items:center;gap:10px">
  <span class="brand-dot"></span>
  <span class="brand-name">NORTHVALE LOAN<span class="brand-sub">LOAN PARTNERS, LLC</span></span>
</div>
<p class="abs foot-text" style="left:188px;top:3935px;width:286px">Northvale Loan is a private investment firm unique in its dual focus on life science and technology credit opportunities. Our ambidextrous approach to investing reflects a broad recognition and appreciation for the critical role intellectual property plays in the successful commercialization of products. We apply our extensive industry.</p>
<div class="abs social"><span></span><span></span><span></span><span></span><span></span></div>

<h3 class="abs foot-title" style="left:526px;top:3872px;width:260px">Our Newsletter</h3>
<div class="abs sec-mark" style="left:647px;top:3914px"></div>
<p class="abs foot-text" style="left:526px;top:3943px;width:260px">Stay contact with northvaleloan latest news.</p>
<div class="abs email-field">Enter Your Email*</div>
<div class="abs btn-send">SEND NOW</div>

<h3 class="abs foot-title" style="left:795px;top:3872px;width:260px">Our Contacts</h3>
<div class="abs sec-mark" style="left:916px;top:3914px"></div>
<p class="abs foot-text" style="left:795px;top:3943px;width:260px">Stay contact with northvaleloan latest news.</p>
<div class="abs contact-line" style="left:872px;top:3974px">
  <svg width="10" height="10" viewBox="0 0 10 10"><path d="M2 1l2 2-1 1.5a6 6 0 0 0 2.5 2.5L7 6l2 2-1.5 1.5C4 9 1 6 .5 2.5z" fill="#d0ab4a"/></svg>+1 (555) 010-4821
</div>
<div class="abs contact-line" style="left:858px;top:4004px">
  <svg width="10" height="8" viewBox="0 0 10 8"><rect width="10" height="8" fill="#d0ab4a"/><path d="M0 0l5 4 5-4" stroke="#1e1f21" fill="none"/></svg>inquiries@northvaleloan.com
</div>
<div class="abs contact-line" style="left:842px;top:4031px">
  <svg width="8" height="11" viewBox="0 0 8 11"><path d="M4 0a4 4 0 0 1 4 4c0 3-4 7-4 7S0 7 0 4a4 4 0 0 1 4-4z" fill="#d0ab4a"/><circle cx="4" cy="4" r="1.5" fill="#1e1f21"/></svg>
  <span style="line-height:15px;text-align:center">220 Harlow Street #310 San<br>Francisco, CA 94107</span>
</div>
<div class="abs to-top"><svg width="20" height="12" viewBox="0 0 20 12"><path d="M2 10l8-8 8 8" stroke="#fff" stroke-width="2" fill="none"/></svg></div>

<div class="abs foot-rule"></div>
<div class="abs copyright">© 2015 Northvale Loan Partners LLC. All Rights Reserved.</div>
<nav class="abs foot-nav"><a href="#">HOME</a><a href="#">STRATEGY</a><a href="#">ABOUT US</a><a href="#">INVESTORS</a><a href="#">CONTACT</a></nav>

</body>
</html>
```